Business Card for innovative, tech/consultant company

We are specializing in bringing together Efficiency methodology and Technology for our Business customers. We would like an astonishing business Card that matches this idea.

Target Market(s)

Businesses of medium size or more

Industry/Entity Type

Business Consultant

Contact Information for Business Card

Name, Title, personal email, www, address, phone

Font styles to use
Sans Serif

Colors
3277b5

Requirements
Must have
• - innovative, efficient design
• - good readable
• - Colors must match our logo (blue and grey)
• - the attached font (is licensed by our Company) must be used (Syntax LT)
Should not have
• overloaded

```html
<!DOCTYPE html>
<html lang="en">
<head>
<meta charset="utf-8">
<title>Keystep Business Card</title>
<link rel="stylesheet" href="https://fonts.googleapis.com/css2?family=Source+Sans+3:wght@400;600;700&display=swap">
<style>
  :root {
    --backdrop: #eceae6;
    --card-white: #ffffff;
    --brand-grey: #7b7c80;
    --band-grey: #9a9b9f;
    --blue-light: #4aa3dd;
    --blue: #1a85cc;
    --blue-deep: #0f78c0;
    --text-on-blue: #ffffff;
    --text-grey: #6d6e72;
  }
  * { box-sizing: border-box; margin: 0; padding: 0; }
  html, body {
    width: 1200px;
    height: 902px;
    overflow: hidden;
    background: var(--backdrop);
    font-family: "Source Sans 3", sans-serif;
  }
  .canvas {
    position: relative;
    width: 1200px;
    height: 902px;
    display: flex;
    align-items: center;
    justify-content: center;
  }
  .business-card {
    position: relative;
    width: 1000px;
    height: 572px;
    background: var(--card-white);
    border-radius: 14px;
    overflow: hidden;
    box-shadow: 0 18px 40px rgba(0,0,0,0.14);
  }
  .card-top {
    position: absolute;
    left: 0; top: 0;
    width: 100%;
    height: 330px;
  }
  .brand-name {
    position: absolute;
    top: 78px;
    left: 0; right: 0;
    text-align: center;
    font-size: 150px;
    font-weight: 400;
    line-height: 1;
    letter-spacing: -2px;
    color: var(--brand-grey);
  }
  .address {
    position: absolute;
    left: 48px;
    bottom: 22px;
    display: flex;
    align-items: center;
    gap: 10px;
    font-size: 28px;
    color: var(--text-grey);
  }
  .address svg { width: 18px; height: 26px; fill: var(--blue); }
  .grey-band {
    position: absolute;
    left: 0; top: 330px;
    width: 100%;
    height: 14px;
    background: var(--band-grey);
  }
  .card-bottom {
    position: absolute;
    left: 0; top: 344px;
    width: 100%;
    height: 228px;
    background: linear-gradient(100deg, var(--blue-light) 0%, var(--blue) 40%, var(--blue-deep) 100%);
    color: var(--text-on-blue);
  }
  .person {
    position: absolute;
    left: 110px;
    top: 44px;
  }
  .person-name {
    font-size: 44px;
    font-weight: 700;
    line-height: 1.1;
  }
  .person-title {
    font-size: 36px;
    font-weight: 400;
    line-height: 1.15;
  }
  .contact-list {
    position: absolute;
    right: 70px;
    top: 30px;
    list-style: none;
    display: flex;
    flex-direction: column;
    gap: 10px;
  }
  .contact-item {
    display: flex;
    align-items: center;
    gap: 14px;
    font-size: 28px;
    font-weight: 400;
  }
  .contact-item svg {
    width: 24px; height: 24px;
    fill: none;
    stroke: var(--text-on-blue);
    stroke-width: 2;
  }
  .contact-item svg.solid { fill: var(--text-on-blue); stroke: none; }
</style>
</head>
<body>
<main class="canvas">
  <section class="business-card">
    <div class="card-top">
      <div class="brand-name">Keystep</div>
      <div class="address">
        <svg viewBox="0 0 18 26" aria-hidden="true"><path d="M9 0C4 0 0 4 0 9c0 6.5 9 17 9 17s9-10.5 9-17C18 4 14 0 9 0zm0 12.5A3.5 3.5 0 1 1 9 5.5a3.5 3.5 0 0 1 0 7z"/></svg>
        <span>2208 West Lake Avenue</span>
      </div>
    </div>
    <div class="grey-band"></div>
    <div class="card-bottom">
      <div class="person">
        <div class="person-name">Dana Morrow</div>
        <div class="person-title">Manager</div>
      </div>
      <ul class="contact-list">
        <li class="contact-item">
          <svg class="solid" viewBox="0 0 24 24" aria-hidden="true"><path d="M6.6 10.8a15.1 15.1 0 0 0 6.6 6.6l2.2-2.2a1 1 0 0 1 1-.25 11.4 11.4 0 0 0 3.6.57 1 1 0 0 1 1 1V20a1 1 0 0 1-1 1A17 17 0 0 1 3 4a1 1 0 0 1 1-1h3.5a1 1 0 0 1 1 1c0 1.25.2 2.45.57 3.57a1 1 0 0 1-.25 1z"/></svg>
          <span>555 210 4836</span>
        </li>
        <li class="contact-item">
          <svg viewBox="0 0 24 24" aria-hidden="true"><circle cx="12" cy="12" r="10"/><ellipse cx="12" cy="12" rx="4.5" ry="10"/><path d="M2 12h20M4 7h16M4 17h16"/></svg>
          <span>www.danamorrow.com</span>
        </li>
        <li class="contact-item">
          <svg viewBox="0 0 24 24" aria-hidden="true"><circle cx="12" cy="12" r="4"/><path d="M16 8v5.5a2.5 2.5 0 0 0 5 0V12a9 9 0 1 0-3.5 7.1"/></svg>
          <span>dana@morrowmail.com</span>
        </li>
      </ul>
    </div>
  </section>
</main>
</body>
</html>
```